Coastal Rubdown Oil Co. needs a new label.

This massage oil has been in Australia for over 20 years and needs a new label for its plastic 250ml bottles. The current label (8cm x 8cm) looks old fashioned and so we are looking for something that reflects freedom, relaxation, inspiration. The product is made from sweet almond oil and has different essential oils used to give unique smells. I have seen some lovely abstract vector images. I think we need a clean straight look with bright colours. There are currently six variations to the product. "Calm and Quiet Heads, Achy and Weary Limbs, Sweethearts Mix, Jasmine Soak Oil, Unwind Mixture, Up-Lifting Mixture" Different coloured labels have been used for each of the blends. I have included photos of existing bottles plus some ideas for the labels.

I would like to use the same font on the name of the brand Quorby Meadow. If we change the font it may be difficult for existing customers to find our product.

Also just under the name Quorby Meadow I would like to insert a type of logo (can be the shape of a tear drop or round circle) to say:

Massage Oil
Since 1970

The size of the label is 8cm x 12 cm for the front and the same size for the back of the label.
Updates

Coastal Rubdown oil Company has posted on the brief some images from Pixmarket plus two photos of the original bottles. I am looking for a new design which is bright in colour, fun and funky. I am not thinking along the lines of the traditional Herb and trees look. I think the original label is too busy and the colours overpower the label. The other point I think that is important is that the product has been around since 1970. If there is room I think a round logo which says: Massage Oil Since 1970 I am hoping that we can fit this information on the label Looking forward to seeing all the designs come thru. So far I have only had two designs come thru. Speak soon from hot sunny Australia. delia

Thank you to everyone who has already posted designs for our Massage Label. I have now edited the brief to include some more ideas on how to make this design the Best! I will email back to you straight away ideas and thoughts on your designs. Remember I live in Australia and can be either 10hrs in front or behind your time.

Project Deadline Extended
Reason: Due to busy lives and commitments over the next few days I feel that an extension will benefit all involved. Thank you to everyone who has submitted designs and working with me to create something beautiful. delia

Hello from Australia all the designers who have submitted some wonderful designs over the past two weeks. We are now entering the final three days of the competition. Thank you to everyone who has worked so hard to try and create the perfect label for my massage oil bottle. All of you have done a fantastic job. This has made the decision hard to make. Thank you to everyone. Please submit all your last minute designs soon. kind regards delia Australia

Target Market(s)

The type of person purchasing a massage oil blend will buy from a health food shop, pharmacy or from an on-line store. I believe they are wanting something bright that clearly communicates that that it is a massage oil.

Industry/Entity Type

Massage

Font styles to use
Script

Requirements
Must have
• Different colour for each massage oil blend.
Need same font for the name Quorby Meadow. (script font or similar)

Abstract design please.
Nice to have
• A logo under the name Quorby Meadow

Tear Drop or circle design that says:

Massage Oil
Since 1970

also we would like an outline for the back label. (see photo attached)

BACK LABEL information

A unique blend of essential oils in a fine light base.

Contains:

vegetable oil extract of nettle, sweet almond oil, ethanol, essential oils of lavender, lemongrass, orange & ylang ylang and vitamin E.

How to Use:

Shake well warm bottle in warm water if very cold.
Lovingly massage the body from head to toe.
Not for medicinal use.

Quorby Meadow
Pellow WA 6143
Phone: (08) 9472 1538

(LEAVE ROOM FOR BARCODE)
Should not have
• Too busy design or old fashioned design.
No dull colours.

```html
<!DOCTYPE html>
<html lang="en">
<head>
<meta charset="utf-8">
<title>Quorby Meadow – Massage Oil Labels</title>
<link rel="stylesheet" href="https://fonts.googleapis.com/css2?family=Great+Vibes&family=Dancing+Script:wght@500&display=swap">
<style>
  :root {
    --canvas: #ffffff;
    --ink: #1a1a1a;
    --cream: #fffbe8;
    --sun: #ffd21a;
    --seal: #e9a21a;
    --seal-text: #ffffff;

    --green: #3cb034;   --green-title: #1f7a2e;
    --pink: #e0137f;    --pink-title: #e3137c;
    --purple: #8b2b8f;  --purple-title: #6b2b82;
    --orange: #ee5a1c;  --orange-title: #e31a1e;
    --ember: #cf2f16;   --ember-title: #b8151b;
    --sky: #1d98da;     --sky-title: #1c5aa8;
  }
  * { box-sizing: border-box; margin: 0; padding: 0; }
  html, body { width: 1200px; height: 1000px; overflow: hidden; background: var(--canvas); }
  .sheet { position: relative; width: 1200px; height: 1000px; }

  .label {
    position: absolute;
    width: 279px; height: 419px;
    overflow: hidden;
    background:
      radial-gradient(ellipse 60% 32% at 50% 2%, #ffffff 0%, rgba(255,255,255,0.85) 40%, rgba(255,255,255,0) 100%),
      radial-gradient(ellipse 40% 55% at 50% 55%, rgba(255,244,170,0.9) 0%, rgba(255,230,90,0) 100%),
      linear-gradient(90deg, var(--side) 0%, rgba(255,255,255,0) 36%, rgba(255,255,255,0) 64%, var(--side) 100%),
      linear-gradient(180deg, var(--cream) 0%, var(--sun) 55%, var(--sun) 100%);
  }
  .label--unwind      { left: 167px; top: 97px;  --side: var(--green);  --title: var(--green-title);
    background:
      radial-gradient(ellipse 60% 32% at 50% 2%, #fff 0%, rgba(255,255,255,0.85) 40%, rgba(255,255,255,0) 100%),
      radial-gradient(ellipse 55% 35% at 10% 100%, var(--green) 0%, rgba(60,176,52,0) 100%),
      radial-gradient(ellipse 40% 60% at 0% 45%, var(--green) 0%, rgba(60,176,52,0) 100%),
      radial-gradient(ellipse 30% 40% at 100% 100%, var(--green) 0%, rgba(60,176,52,0) 100%),
      linear-gradient(180deg, var(--cream) 0%, #e8e21a 55%, #f2d816 100%); }
  .label--sweethearts { left: 487px; top: 97px;  --side: var(--pink);   --title: var(--pink-title); }
  .label--jasmine     { left: 807px; top: 98px;  --side: var(--purple); --title: var(--purple-title); }
  .label--uplifting   { left: 167px; top: 553px; --side: var(--orange); --title: var(--orange-title); }
  .label--limbs       { left: 493px; top: 555px; --side: var(--ember);  --title: var(--ember-title); }
  .label--heads       { left: 811px; top: 557px; --side: var(--sky);    --title: var(--sky-title); }

  .brand { position: absolute; left: 0; top: 18px; width: 100%; text-align: center;
    font-family: "Great Vibes", cursive; color: var(--ink); font-weight: 400; }
  .brand-main { display: block; font-size: 46px; line-height: 1; margin-left: -20px; }
  .brand-sub  { display: block; font-size: 30px; line-height: 1; margin-left: 80px; margin-top: -2px; }

  .seal { position: absolute; left: 89px; top: 150px; width: 102px; height: 102px;
    border-radius: 50%; background: var(--seal);
    display: flex; align-items: center; justify-content: center; text-align: center;
    font-family: Arial, Helvetica, sans-serif; font-size: 11px; line-height: 1.2; color: var(--seal-text); }

  .accent { position: absolute; width: 26px; height: 22px; border-radius: 50%;
    background: radial-gradient(circle, rgba(255,255,255,0.95) 0%, rgba(255,255,255,0) 75%); }
  .accent--left  { left: 60px;  top: 160px; }
  .accent--right { left: 195px; top: 128px; }

  .blend { position: absolute; left: 0; top: 268px; width: 100%; text-align: center;
    font-family: "Dancing Script", cursive; font-weight: 500; color: var(--title);
    font-size: 33px; line-height: 42px; }
  .blend--long { font-size: 28px; }
  .blend-second--small { font-size: 26px; }

  .volume { position: absolute; left: 0; top: 382px; width: 100%; text-align: center;
    font-family: Arial, Helvetica, sans-serif; font-size: 11px; color: var(--ink); }
</style>
</head>
<body>
<main class="sheet">

  <section class="label label--unwind">
    <div class="brand"><span class="brand-main">Quorby</span><span class="brand-sub">Meadow</span></div>
    <span class="accent accent--left" role="img" aria-label="White butterfly"></span>
    <span class="accent accent--right" role="img" aria-label="White butterfly"></span>
    <p class="seal">Massage Oil<br>Since 1970</p>
    <h2 class="blend"><span>Unwind</span><br><span>Mixture</span></h2>
    <p class="volume">250ml</p>
  </section>

  <section class="label label--sweethearts">
    <div class="brand"><span class="brand-main">Quorby</span><span class="brand-sub">Meadow</span></div>
    <span class="accent accent--left" role="img" aria-label="White butterfly"></span>
    <span class="accent accent--right" role="img" aria-label="White butterfly"></span>
    <p class="seal">Massage Oil<br>Since 1970</p>
    <h2 class="blend"><span>Sweethearts</span><br><span>Mix</span></h2>
    <p class="volume">250ml</p>
  </section>

  <section class="label label--jasmine">
    <div class="brand"><span class="brand-main">Quorby</span><span class="brand-sub">Meadow</span></div>
    <span class="accent accent--left" role="img" aria-label="White butterfly"></span>
    <span class="accent accent--right" role="img" aria-label="White butterfly"></span>
    <p class="seal">Massage Oil<br>Since 1970</p>
    <h2 class="blend"><span>Jasmine</span><br><span class="blend-second--small">Soak Oil</span></h2>
    <p class="volume">250ml</p>
  </section>

  <section class="label label--uplifting">
    <div class="brand"><span class="brand-main">Quorby</span><span class="brand-sub">Meadow</span></div>
    <span class="accent accent--left" role="img" aria-label="White butterfly"></span>
    <span class="accent accent--right" role="img" aria-label="White butterfly"></span>
    <p class="seal">Massage Oil<br>Since 1970</p>
    <h2 class="blend"><span>Up-Lifting</span><br><span>Mixture</span></h2>
    <p class="volume">250ml</p>
  </section>

  <section class="label label--limbs">
    <div class="brand"><span class="brand-main">Quorby</span><span class="brand-sub">Meadow</span></div>
    <span class="accent accent--left" role="img" aria-label="White butterfly"></span>
    <span class="accent accent--right" role="img" aria-label="White butterfly"></span>
    <p class="seal">Massage Oil<br>Since 1970</p>
    <h2 class="blend blend--long"><span>Achy &amp; Weary</span><br><span>Limbs</span></h2>
    <p class="volume">250ml</p>
  </section>

  <section class="label label--heads">
    <div class="brand"><span class="brand-main">Quorby</span><span class="brand-sub">Meadow</span></div>
    <span class="accent accent--left" role="img" aria-label="White butterfly"></span>
    <span class="accent accent--right" role="img" aria-label="White butterfly"></span>
    <p class="seal">Massage Oil<br>Since 1970</p>
    <h2 class="blend blend--long"><span>Calm &amp; Quiet</span><br><span>Heads</span></h2>
    <p class="volume">250ml</p>
  </section>

</main>
</body>
</html>
```